Infographic Design for website

We are currently looking for an infographic that will show the flow of our upcoming graphic design bidding website. The flow of our website will go as followed.

FOR GRAPHIC DESIGNERS

Bid on various projects and start designing for clients around the world. Designers will be able to compete, show off their creativity, and receive their earnings.

How It Works
- Its free for graphic designers to start!
- Graphic designers will be able to build online portfolio
- Clients will post their design request online
- Graphic designers will bid on projects that clients post
- If client rewards graphic designer with project, the graphic designer will then design for client
- After design is complete and client will 100% satisfied, the graphic designer will then collect their earnings from project.

This will be an infographic to show the flow of how our upcoming website will work. The design has to be creative and appealing to the eyes of graphic designers nationwide. Please use flow of our website to create the design, you may switch up the wording if needed. This will be used for advertising and clarification of flow.

Please add our company information:

Company Name: Brightwater Prints & Studios

```html
<!DOCTYPE html>
<html lang="en">
<head>
<meta charset="utf-8">
<title>Brightwater Prints &amp; Studios – How It Works for Graphic Designers</title>
<link rel="stylesheet" href="https://fonts.googleapis.com/css2?family=Playfair+Display+SC:wght@900&family=Righteous&family=Open+Sans:wght@700&display=swap">
<style>
  :root {
    --brand-red: #c8202a;
    --ink: #111111;
    --navy: #0e4a70;
    --coral: #ef5b55;
    --sun: #fddc5c;
    --teal: #6cc3b4;
    --ocean: #21709c;
    --ocean-light: #2a80ab;
    --paper: #ffffff;
    --figure: #1c1c1c;
  }
  html, body {
    margin: 0;
    padding: 0;
    width: 1200px;
    height: 960px;
    overflow: hidden;
    background: var(--paper);
  }
  .infographic {
    display: block;
    width: 1200px;
    height: 960px;
  }
  .brand-name {
    font-family: "Playfair Display SC", "Playfair Display", serif;
    font-weight: 900;
    font-size: 40px;
    fill: var(--brand-red);
  }
  .brand-mark { fill: var(--brand-red); }
  .audience-title {
    font-family: "Righteous", sans-serif;
    font-size: 22px;
    letter-spacing: 2px;
    fill: var(--ink);
  }
  .step-label {
    font-family: "Open Sans", sans-serif;
    font-weight: 700;
    font-size: 15px;
    fill: var(--paper);
  }
  .icon-line { fill: none; stroke: var(--paper); stroke-width: 3; stroke-linecap: round; stroke-linejoin: round; }
  .icon-fill { fill: var(--paper); }
  .step-navy { fill: var(--navy); }
  .step-coral { fill: var(--coral); }
  .step-sun { fill: var(--sun); }
  .step-teal { fill: var(--teal); }
  .step-ocean { fill: var(--ocean); }
  .step-ocean-light { fill: var(--ocean-light); }
  .designer-figure { fill: var(--figure); opacity: 0.88; }
</style>
</head>
<body>
<svg class="infographic" viewBox="0 0 900 720" width="1200" height="960" xmlns="http://www.w3.org/2000/svg">

  <!-- Header -->
  <g class="header">
    <circle class="brand-mark" cx="160" cy="38" r="20"/>
    <text class="brand-name" x="194" y="53" textLength="620" lengthAdjust="spacingAndGlyphs">Brightwater Prints &amp; Studios</text>
    <text class="audience-title" x="458" y="114" text-anchor="middle">FOR GRAPHIC DESIGNER</text>
  </g>

  <!-- Top row: steps flowing left -->
  <g class="flow-top">
    <polygon class="step-sun" points="540,258 580,222 580,235 795,235 795,392 771,372 748,392 748,281 580,281 580,294"/>
    <polygon class="step-coral" points="340,258 380,222 380,235 560,235 538,258 560,281 380,281 380,294"/>
    <polygon class="step-navy" points="160,258 203,222 203,235 362,235 340,258 362,281 203,281 203,294"/>

    <text class="step-label" x="268" y="264" text-anchor="middle">EARNING</text>
    <text class="step-label" x="450" y="264" text-anchor="middle">REWARD PROJECT</text>
    <text class="step-label" x="640" y="264" text-anchor="middle">PLACE BID</text>

    <!-- Earning marker -->
    <rect class="step-navy" x="263" y="208" width="10" height="28"/>
    <circle class="step-navy" cx="268" cy="185" r="27"/>
    <path class="icon-fill" d="M262 170 h12 l-3 6 q12 6 12 18 q0 8 -10 8 h-10 q-10 0 -10 -8 q0 -12 12 -18 z"/>
    <text x="268" y="199" text-anchor="middle" font-family="Open Sans, sans-serif" font-weight="700" font-size="13" fill="#0e4a70">$</text>

    <!-- Reward marker -->
    <rect class="step-coral" x="436" y="208" width="10" height="28"/>
    <circle class="step-coral" cx="441" cy="185" r="27"/>
    <path class="icon-fill" d="M431 172 h20 v8 q0 10 -10 12 q-10 -2 -10 -12 z"/>
    <path class="icon-line" d="M431 175 h-5 q0 8 7 9 M451 175 h5 q0 8 -7 9"/>
    <rect class="icon-fill" x="439" y="192" width="4" height="6"/>
    <rect class="icon-fill" x="433" y="198" width="16" height="4"/>

    <!-- Bid marker -->
    <rect class="step-sun" x="631" y="208" width="10" height="28"/>
    <circle class="step-sun" cx="636" cy="185" r="27"/>
    <rect class="icon-fill" x="628" y="167" width="18" height="16" rx="2"/>
    <path d="M632 175 l4 4 l7 -8" fill="none" stroke="#fddc5c" stroke-width="2.5" stroke-linecap="round" stroke-linejoin="round"/>
    <path class="icon-fill" d="M624 190 h12 l6 -4 v14 h-18 z"/>
  </g>

  <!-- Designer at desk -->
  <rect class="designer-figure" x="390" y="312" width="180" height="160" rx="12" role="img" aria-label="Silhouette of a graphic designer seated at a desk working at a computer"/>

  <!-- Bottom row: steps flowing right -->
  <g class="flow-bottom">
    <polygon class="step-ocean-light" points="725,486 748,486 748,400 771,378 795,400 795,545 725,545 745,518"/>
    <polygon class="step-coral" points="160,486 322,486 322,474 365,518 322,562 322,550 160,550 183,518"/>
    <polygon class="step-teal" points="345,486 508,486 508,474 550,518 508,562 508,550 345,550 368,518"/>
    <polygon class="step-ocean" points="540,486 700,486 700,474 745,518 700,562 700,550 540,550 563,518"/>

    <text class="step-label" x="250" y="524" text-anchor="middle">START</text>
    <text class="step-label" x="445" y="524" text-anchor="middle">ONLINE PORTFOLIO</text>
    <text class="step-label" x="645" y="524" text-anchor="middle">PROJECT REQUEST</text>

    <!-- Start marker -->
    <rect class="step-coral" x="253" y="548" width="10" height="20"/>
    <circle class="step-coral" cx="258" cy="592" r="27"/>
    <polygon class="icon-fill" points="251,580 269,592 251,604"/>

    <!-- Portfolio marker -->
    <rect class="step-teal" x="428" y="548" width="10" height="20"/>
    <circle class="step-teal" cx="433" cy="592" r="27"/>
    <rect class="icon-line" x="427" y="579" width="12" height="6" rx="2"/>
    <rect class="icon-fill" x="419" y="584" width="28" height="20" rx="3"/>
    <rect x="419" y="592" width="28" height="2" fill="#6cc3b4"/>

    <!-- Request marker -->
    <rect class="step-ocean" x="623" y="548" width="10" height="20"/>
    <circle class="step-ocean" cx="628" cy="592" r="27"/>
    <rect class="icon-fill" x="624" y="577" width="7" height="20" rx="3.5"/>
    <path class="icon-fill" d="M620 593 h22 v8 q0 8 -8 8 h-8 q-6 0 -6 -6 z"/>
  </g>
</svg>
</body>
</html>
```